New Template design for Website in Wordpress

We are interested in changing our website look at www.cargolinx.com -We also are very interested in Have it done in Wordpress in which we are understanding the search engines are liking a bit more. The website we would want to try working with on this is www.cargolinx.com. We look forward to seeing the different design ideas please just make sure they are in wordpress! Thanks, Marlen

Reason: need more design idea..... We would still like to use our pictures off our site since we paid for them so keep that in mind as well as we would still want the rotating pictures in the head of the page but not in Flash.

```html
<!DOCTYPE html>
<html lang="en">
<head>
<meta charset="utf-8">
<title>CargoLinx — Worldwide Shipping</title>
<link href="https://fonts.googleapis.com/css2?family=Open+Sans:wght@400;600;700&family=Roboto+Condensed:wght@700&display=swap" rel="stylesheet">
<style>
:root{
  --red:#d6262b;
  --orange:#f7a21b;
  --blue:#1d8fe0;
  --ink:#2b2b2b;
  --muted:#666;
  --line:#dcdcdc;
  --footer:#1f1f1f;
  --white:#fff;
}
*{box-sizing:border-box;margin:0;padding:0}
html,body{width:1200px;height:2685px;overflow:hidden}
body{font-family:"Open Sans",Arial,sans-serif;color:var(--ink);background:var(--white);position:relative}
.wrap{width:880px;margin:0 auto;position:relative}

/* header */
.site-header{height:80px;position:relative}
.brand{position:absolute;left:0;top:18px;display:flex;align-items:center;gap:10px}
.brand-mark{width:14px;height:14px;background:var(--red)}
.brand-name{font-weight:600;font-size:26px;color:var(--ink);line-height:1}
.brand-tag{position:absolute;left:0;top:52px;font-size:10px;color:#666;letter-spacing:.3px;white-space:nowrap}
.contact-bar{position:absolute;right:0;top:9px;display:flex;align-items:center;gap:8px;font-size:12px;color:#888}
.contact-bar b{color:var(--red);font-weight:600}
.social-dot{width:18px;height:18px;border:1px solid #bbb;border-radius:50%}
.main-nav{position:absolute;right:0;top:44px;display:flex;gap:26px;font-size:13px;color:#444}
.main-nav .active{color:var(--red)}

/* hero */
.hero{height:578px;position:relative;overflow:hidden;
  background:linear-gradient(180deg,#6d8aa6 0%,#4d6c8c 30%,#2f4c6c 65%,#27415e 100%)}
.hero-photo{position:absolute;inset:0;background:linear-gradient(120deg,rgba(180,60,50,.55) 10%,rgba(60,70,80,.2) 45%,rgba(30,50,80,0) 70%)}
.hero-copy{position:absolute;left:0;right:0;top:165px;text-align:center;color:var(--white)}
.hero-title{font-family:"Roboto Condensed",Arial,sans-serif;font-size:46px;line-height:1.1;text-shadow:0 2px 4px rgba(0,0,0,.5)}
.hero-title .hl-trucking{color:var(--orange)}
.hero-title .hl-ocean{color:var(--red)}
.hero-lead{font-size:15px;margin-top:12px;text-shadow:0 1px 3px rgba(0,0,0,.6)}
.btn{display:inline-block;font-weight:700;color:var(--white);background:var(--blue);border-radius:3px}
.hero .btn{margin-top:34px;padding:14px 26px;font-family:"Roboto Condensed",Arial,sans-serif;font-size:24px;background:#14a4e0}
.slider-dots{position:absolute;left:50%;bottom:22px;transform:translateX(-50%);display:flex;gap:8px}
.slider-dots span{width:10px;height:10px;border-radius:50%;background:rgba(255,255,255,.6);border:1px solid #fff}
.slider-dots span.on{background:var(--red)}

/* services */
.services{height:532px;padding-top:52px}
.service-grid{display:flex;gap:25px}
.service-card{width:202px;border:1px solid var(--line);text-align:center;height:445px;position:relative}
.service-img{height:188px}
.img-heavy{background:linear-gradient(180deg,#9dbad8,#c9a23a 60%,#7a6a4b)}
.img-dry{background:linear-gradient(180deg,#5b8fc9,#dfe6ee 55%,#8a8f92)}
.img-flat{background:linear-gradient(180deg,#a8c6e4,#9aa8b4 55%,#6a7d4a)}
.img-ocean{background:linear-gradient(180deg,#7aa6d0,#b94b3c 50%,#1f4a78)}
.service-title{font-size:17px;font-weight:600;line-height:1.25;margin:20px 10px 8px;color:#222}
.service-text{font-size:11.5px;line-height:1.5;color:var(--muted);padding:0 14px}
.btn-outline{position:absolute;left:50%;bottom:14px;transform:translateX(-50%);border:1px solid #bbb;padding:6px 16px;font-size:10.5px;font-weight:700;color:var(--red);border-radius:2px;white-space:nowrap}

/* about */
.about{height:430px;position:relative;color:var(--white);text-align:center;
  background:linear-gradient(90deg,#2c2c2c,#3a3631 55%,#4a3d30);
  clip-path:polygon(0 0,100% 0,100% 100%,0 93%)}
.about-title{padding-top:38px;font-size:32px;font-weight:600}
.about-sub{font-size:17px;font-weight:600;margin-top:2px}
.about-text{font-size:12.5px;line-height:1.65;margin:28px auto 0;width:880px;color:#ddd}
.about-text+.about-text{margin-top:14px}
.about .btn{margin-top:28px;padding:13px 32px;font-size:17px}

/* link columns */
.links{height:290px;padding-top:40px}
.link-row{display:flex;justify-content:space-between}
.link-col{width:210px;text-align:center}
.link-col h3{font-size:17px;font-weight:600;padding-bottom:12px;border-bottom:2px solid var(--line);position:relative;white-space:nowrap}
.link-col h3::after{content:"";position:absolute;left:50%;bottom:-2px;width:60px;margin-left:-30px;height:2px;background:var(--red)}
.link-col li{list-style:none;font-size:11.5px;color:#555;padding:8px 0;border-bottom:1px solid #eee;white-space:nowrap}
.social-box{width:202px;border:1px solid var(--line);height:210px}
.social-box .box-head{background:#eceff5;font-size:11px;font-weight:700;padding:6px 8px;color:#333}
.social-box .box-name{font-size:14px;color:var(--red);font-weight:700;padding:8px 8px 4px}
.social-box .box-meta{font-size:10px;color:#777;padding:0 8px 6px}
.member-grid{display:grid;grid-template-columns:repeat(5,30px);gap:6px;padding:4px 8px}
.member-grid span{height:30px;background:linear-gradient(135deg,#9a7d6a,#5a4a40)}
.social-box .box-foot{font-size:10px;color:#555;padding:8px}

/* testimonials */
.testimonials{height:345px;position:relative;color:var(--white);text-align:center;
  background:linear-gradient(180deg,#3c3b38,#23262a 60%,#1c1e20);
  clip-path:polygon(0 7%,100% 0,100% 100%,0 100%)}
.testimonials h2{padding-top:44px;font-size:30px;font-weight:600}
.avatars{display:flex;justify-content:center;align-items:center;gap:10px;margin-top:16px}
.avatar{width:46px;height:46px;border-radius:50%;border:3px solid #fff;background:#8a7160}
.avatar.main{width:64px;height:64px;background:#6d5a4c}
.quote{font-size:12.5px;line-height:1.7;color:#ddd;width:880px;margin:22px auto 0}
.quote-name{margin-top:14px;font-size:12px;font-weight:700}

/* contact */
.contact{height:300px;text-align:center}
.contact h2{padding-top:52px;font-size:34px;font-weight:400}
.contact-lead{font-size:12.5px;color:var(--muted);width:520px;margin:10px auto 0;line-height:1.55}
.contact-row{display:flex;justify-content:space-between;width:800px;margin:40px auto 0}
.contact-item{width:200px}
.contact-item svg{display:block;margin:0 auto 6px}
.contact-item .label{font-size:14px;font-weight:700}
.contact-item .value{font-size:12.5px;color:#444;margin-top:4px}

/* footer */
.site-footer{height:130px;background:var(--footer);color:#bbb;font-size:10.5px;line-height:1.6}
.site-footer .wrap{display:flex;justify-content:space-between;padding-top:22px}
.footer-left{width:400px}
.footer-left p+p{margin-top:14px}
.footer-right{text-align:right}
.footer-right p+p{margin-top:14px}
</style>
</head>
<body>

<header class="site-header">
  <div class="wrap">
    <div class="brand">
      <span class="brand-mark"></span>
      <span class="brand-name">CargoLinx</span>
    </div>
    <div class="brand-tag">Trucking &amp; Ocean Logistics</div>
    <div class="contact-bar">Call Now: <b>(888) 555-0142</b>
      <span class="social-dot"></span><span class="social-dot"></span><span class="social-dot"></span>
    </div>
    <nav class="main-nav">
      <span class="active">Home</span><span>Insurance &amp; Legal Info</span><span>Fast Freight Quote</span>
    </nav>
  </div>
</header>

<section class="hero">
  <div class="hero-photo" role="img" aria-label="Container ship loaded with stacked cargo containers sailing on the ocean"></div>
  <div class="hero-copy">
    <h1 class="hero-title">Worldwide Shipping<br><span class="hl-trucking">Trucking</span> and <span class="hl-ocean">Ocean</span> Service with No Limits</h1>
    <p class="hero-lead">We are a one stop solution logistics company servicing Worldwide with our Trucking and Ocean shipping service.</p>
    <span class="btn">Get a Freight Quote</span>
  </div>
  <div class="slider-dots"><span class="on"></span><span></span><span></span></div>
</section>

<section class="services">
  <div class="wrap service-grid">
    <article class="service-card">
      <div class="service-img img-heavy" role="img" aria-label="Heavy mining truck carried on a lowboy trailer"></div>
      <h3 class="service-title">Heavy Haul<br>Services</h3>
      <p class="service-text">No Limits on Equipment Weight and Size - All Machinery or Equipment transported covered to full value. We will transport all of your Oversized &amp; Heavy equipment &amp; machinery in a...</p>
      <span class="btn-outline">LEARN MORE</span>
    </article>
    <article class="service-card">
      <div class="service-img img-dry" role="img" aria-label="White semi truck with a dry van trailer on the highway"></div>
      <h3 class="service-title">Dry &amp; Refrigerated<br>Services</h3>
      <p class="service-text">We currently offer dry van / box van service to all 48 States and Canada. Our Dry Van lengths start at 24' and go up to 53' in length. Full loads for Dry Van freight usually max out...</p>
      <span class="btn-outline">LEARN MORE</span>
    </article>
    <article class="service-card">
      <div class="service-img img-flat" role="img" aria-label="Flatbed trucks carrying loads along a highway"></div>
      <h3 class="service-title">Flatbed, Step Deck &amp;<br>Piggy Back Service</h3>
      <p class="service-text">With thousands of flatbeds transporting freight for our customers from coast to coast, we provide some of the most competitive rates in the industry, today. Our flatbeds transport...</p>
      <span class="btn-outline">LEARN MORE</span>
    </article>
    <article class="service-card">
      <div class="service-img img-ocean" role="img" aria-label="Cargo ship with colourful containers at sea"></div>
      <h3 class="service-title">Freight Forwarding<br>Ocean Services</h3>
      <p class="service-text">Whether you need a freight quote for a full load, LTL/Partial load, or Oversized Machinery or Equipment, trucking and/or ocean shipment, we will take care of it. All your freight or...</p>
      <span class="btn-outline">LEARN MORE</span>
    </article>
  </div>
</section>

<section class="about" role="img" aria-label="Dark backdrop of a freight truck at a port terminal">
  <h2 class="about-title">About CargoLinx</h2>
  <p class="about-sub">Worldwide shipping- Ocean and Trucking with no limits</p>
  <p class="about-text">Welcome to CargoLinx and Nightline Haulers Inc. We are a one stop solution logistics company servicing Worldwide with our Trucking and Ocean shipping service. In using our freight services, we will negotiate a competitive freight quote using over 5000 different carriers who are certified and contracted by us. We have all equipment types available daily, service all freight types, and have no limits Worldwide.</p>
  <p class="about-text">Whether you need a freight quote for a full load, LTL/Partial load, or Oversized Machinery or Equipment, trucking and/or ocean shipment, we will take care of it. All your freight or equipment to be shipped will be covered in full by our insurance with no limitations to match its value. We manage the calls, the paperwork, and the headaches, and you get your freight moved with no hassle at a competitive shipping price!</p>
  <span class="btn">Get Fast &amp; Free Freight Quotes Online in 2 minute</span>
</section>

<section class="links">
  <div class="wrap link-row">
    <div class="link-col">
      <h3>Freight Services</h3>
      <ul><li>Freight Service Areas</li><li>Truck Equipment Types</li><li>Insurance &amp; Legal Details</li><li>Get a Freight Quote Now!</li><li>Return to Home Page</li></ul>
    </div>
    <div class="link-col">
      <h3>Truck Types Available</h3>
      <ul><li>Heavy Equipment Hauling</li><li>LTL Freight Transport</li><li>Flatbed Transport</li><li>Step Deck Transport</li><li>Dry Van Transport</li></ul>
    </div>
    <div class="link-col">
      <h3>We Ship It All!</h3>
      <ul><li>Full Loads</li><li>LTL- Less Than Full Loads</li><li>Oversized &amp; Overweight Loads</li><li>500 LBS to 200,000 LBS (No Limits)</li><li>Construction &amp; Mining Equipment</li></ul>
    </div>
    <div class="social-box">
      <div class="box-head">Find us online</div>
      <div class="box-name">CargoLinx</div>
      <div class="box-meta">1,046 people follow CargoLinx</div>
      <div class="member-grid" role="img" aria-label="Grid of follower profile pictures">
        <span></span><span></span><span></span><span></span><span></span>
        <span></span><span></span><span></span><span></span><span></span>
      </div>
      <div class="box-foot">Follow our page for updates</div>
    </div>
  </div>
</section>

<section class="testimonials" role="img" aria-label="Dusk photo of a truck on an open road">
  <h2>What Customers Are Saying?</h2>
  <div class="avatars">
    <span class="avatar" role="img" aria-label="Customer portrait"></span>
    <span class="avatar main" role="img" aria-label="Customer portrait"></span>
    <span class="avatar" role="img" aria-label="Customer portrait"></span>
  </div>
  <p class="quote">Lorem Ipsum is simply dummy text of the printing and typesetting industry. Lorem Ipsum has been the industry's standard dummy text ever since the 1500s, when an unknown printer took a galley of type and scrambled it to make a type specimen book. It has survived not only five centuries, but also the leap into electronic typesetting, remaining essentially unchanged.</p>
  <p class="quote-name">DANIEL HART</p>
</section>

<section class="contact">
  <h2>Contact us</h2>
  <p class="contact-lead">Lorem Ipsum is simply dummy text of the printing and typesetting industry. Lorem Ipsum has been the industry's standard dummy text ever.</p>
  <div class="contact-row">
    <div class="contact-item">
      <svg width="22" height="22" viewBox="0 0 24 24"><path fill="#d6262b" d="M6.6 10.8a15.1 15.1 0 0 0 6.6 6.6l2.2-2.2c.3-.3.7-.4 1-.2 1.1.4 2.3.6 3.6.6.6 0 1 .4 1 1V20c0 .6-.4 1-1 1A17 17 0 0 1 3 4c0-.6.4-1 1-1h3.5c.6 0 1 .4 1 1 0 1.3.2 2.5.6 3.6.1.3 0 .7-.2 1z"/></svg>
      <div class="label">Call Us</div><div class="value">0400 555 018</div>
    </div>
    <div class="contact-item">
      <svg width="22" height="22" viewBox="0 0 24 24"><path fill="#d6262b" d="M12 3 2 12h3v8h5v-5h4v5h5v-8h3z"/></svg>
      <div class="label">Address</div><div class="value">1349 Rd Lorem Ipsum, USA</div>
    </div>
    <div class="contact-item">
      <svg width="22" height="22" viewBox="0 0 24 24"><path fill="#d6262b" d="M3 5h18v14H3zm2 2v.5l7 4.5 7-4.5V7z"/></svg>
      <div class="label">Email Us</div><div class="value">info@cargolinx.com</div>
    </div>
  </div>
</section>

<footer class="site-footer">
  <div class="wrap">
    <div class="footer-left">
      <p>Full Loads, LTL, Oversized Machinery &amp; Equipment. We do it all. All freight covered to full value by our insurance!</p>
      <p>All freight covered by a minimum of $1,000,000 in Liability and $100,000+ in Cargo insurance with no limits in All 48 States and Canada!</p>
    </div>
    <div class="footer-right">
      <p>Home | Insurance &amp; Legal Info | Fast Freight Quote | Sitemap</p>
      <p>© 2014 CargoLinx, LLC | All Rights Reserved.<br>Owned by Nightline Haulers Inc. and cargolinx.com</p>
    </div>
  </div>
</footer>

</body>
</html>
```